Investigation Tool App - Static Google Ad Image

We need a static image design that promotes our website, which provides an online incident investigation collaboration tool. I would like this static image for Google, but I am also seeking the same design in a LinkedIn Ad ratio.

We would like to see engaging ad graphics that capture the essence of collaboration, time saving, fast "impact-to-learnings" type vibe. As it helps them collaborate and facilitate the investigation on our interactive canvas and then it has an automated report builder that is AI-assisted to turn their information into coherent sentences in the report, it is not fully AI generated (this is important as i feel people inherently distrust AI generated content).

This tool is aimed at safety professionals in mining, construction and oil & gas who want an easy way to facilitate investigations virtually or in person without having to use whiteboards and double handle information and that want to be able to generate a report and learnings on the same day to quickly prevent further harm.

I have included a bunch of snips of my site and features etc - please feel free to use any of them but dont be constrained by these.

Target Market(s)

Safety Professionals/ Managers in Mining, Oil & Gas & Construction

Industry/Entity Type

Mining, Oil & Gas & Construction

Font styles to use
Sans Serif

Requirements
Nice to have
• Modern, pain point focussed, visual of investigation map and or nodes
Should not have
• No em-dashes, no gimmicky language or terms

```html
<!DOCTYPE html>
<html lang="en">
<head>
<meta charset="utf-8">
<title>Norvex Investigation Tool Ad</title>
<link href="https://fonts.googleapis.com/css2?family=Montserrat:ital,wght@0,600;0,800;0,900;1,800;1,900&family=Kalam:wght@400;700&display=swap" rel="stylesheet">
<style>
:root{
  --sky:#29dcfb;
  --grid:rgba(255,255,255,.55);
  --white:#ffffff;
  --ink:#0b0b0b;
  --navy:#06509e;
  --paper:#f7f7f5;
  --panel-line:#bdbdbd;
  --card-line:#d6d6d6;
  --orange:#f7821f;
  --yellow:#f4c21a;
  --purple:#7c4ce0;
  --green:#2fae5a;
  --teal:#14a38f;
  --blue:#1b4fd6;
  --red:#e23b3b;
  --note-yellow:#fbe67c;
  --note-grey:#eeeeea;
  --accent:#8a3cf0;
}
*{margin:0;padding:0;box-sizing:border-box}
html,body{width:1200px;height:628px;overflow:hidden}
body{
  position:relative;
  font-family:"Montserrat",sans-serif;
  background-color:var(--sky);
  background-image:
    linear-gradient(var(--grid) 1.5px,transparent 1.5px),
    linear-gradient(90deg,var(--grid) 1.5px,transparent 1.5px);
  background-size:31px 31px;
  background-position:-2px 6px;
}
.headline{
  position:absolute;left:0;top:32px;width:1200px;text-align:center;
  color:var(--white);font-weight:900;font-style:italic;font-size:47px;
  line-height:52px;letter-spacing:1px;text-shadow:0 0 12px rgba(255,255,255,.55);
}
/* app window */
.app{
  position:absolute;left:73px;top:173px;width:611px;height:287px;
  background-color:var(--paper);
  background-image:
    linear-gradient(#e4e4e4 1px,transparent 1px),
    linear-gradient(90deg,#e4e4e4 1px,transparent 1px);
  background-size:9px 9px;
  box-shadow:0 10px 24px rgba(0,0,0,.25);
  overflow:hidden;
}
.app-bar{height:20px;background:var(--ink);display:flex;align-items:center;padding:0 6px;gap:10px}
.app-name{color:var(--white);font-weight:900;font-style:italic;font-size:10px}
.app-title{color:var(--sky);font-weight:800;font-size:6px;letter-spacing:1px}
.app-bar-right{margin-left:auto;display:flex;align-items:center;gap:5px;font-size:4px;color:var(--white);font-weight:600}
.mode-pill{background:var(--green);padding:1px 3px;border-radius:2px;font-size:3.5px}
.app-gear{width:8px;height:8px;border:1px solid #888;border-radius:50%}
.tool-btn{position:absolute;width:18px;height:18px;background:var(--white);border-radius:4px;box-shadow:0 1px 3px rgba(0,0,0,.2);display:flex;align-items:center;justify-content:center}
.tool-btn.accent{background:var(--accent)}
.panel{position:absolute;border:1px solid var(--panel-line);border-radius:4px;background:rgba(255,255,255,.35)}
.panel-tag{position:absolute;left:6px;top:-3px;width:26px;height:5px;border:1px solid var(--panel-line);border-radius:3px;background:var(--white)}
.card{
  position:absolute;width:38px;height:26px;background:var(--white);
  border:1px solid var(--card-line);border-top:3px solid var(--c,var(--blue));
  background-image:repeating-linear-gradient(#fff 0 3px,#bbb 3px 3.6px,#fff 3.6px 4.5px);
  background-size:30px 15px;background-repeat:no-repeat;background-position:3px 3px;
  box-shadow:0 1px 2px rgba(0,0,0,.1);
}
.card.footed::after{content:"";position:absolute;left:2px;right:2px;bottom:2px;height:3px;background:var(--ink)}
.card.chip::after{content:"";position:absolute;left:3px;right:3px;bottom:2px;height:3px;border:1px solid var(--c);background:#fff}
.person{position:absolute;width:20px;height:20px;border-radius:50%;background:var(--ink);border:2px solid var(--white);outline:1px solid var(--ink)}
/* notes */
.note{position:absolute;font-family:"Kalam",cursive;color:#333;box-shadow:3px 6px 10px rgba(0,0,0,.25)}
.note-collab{left:50px;top:385px;width:115px;height:112px;background:var(--note-grey);transform:rotate(5deg);padding:22px 6px 0 8px}
.note-collab h3{font-size:12px;font-weight:700;text-align:center;margin-bottom:3px}
.note-collab li{list-style:none;font-size:7px;line-height:14px;display:flex;justify-content:space-between}
.note-collab li span{color:var(--red)}
.note-map{left:582px;top:390px;width:108px;height:102px;background:var(--note-yellow);transform:rotate(-6deg);padding:24px 5px 0;text-align:center}
.note-map h3{font-size:11px;font-weight:700;margin-bottom:3px}
.note-map p{font-size:8px;line-height:12px}
.note-map u{font-weight:700}
.pin{position:absolute;width:11px;height:11px;border-radius:50%;background:var(--red)}
/* thumbnails */
.thumb{position:absolute;top:510px;height:78px;box-shadow:0 4px 10px rgba(0,0,0,.2);overflow:hidden}
.thumb-home{left:112px;width:164px;background:#f4f2ee;text-align:center;padding-top:26px}
.thumb-home p{font-size:7.5px;line-height:8px;color:#222;font-weight:600;letter-spacing:-.2px}
.thumb-home p.muted{color:#888}
.thumb-home .btns{display:flex;justify-content:center;gap:4px;margin-top:6px}
.thumb-home .btns i{width:18px;height:3px;background:var(--blue);display:block}
.thumb-home .btns i+i{background:#ccc}
.thumb-style{left:298px;width:163px;background:#eee;display:flex}
.thumb-style .side{width:35px;background:#1b2330;padding:8px 2px}
.thumb-style .spectrum{height:24px;margin-top:18px;background:linear-gradient(90deg,red,orange,yellow,lime,cyan,blue,magenta);}
.thumb-style .sheet{flex:1;position:relative}
.thumb-flow{left:479px;width:118px;background:var(--white)}
/* right column */
.feature{position:absolute;left:770px;display:flex;align-items:center;gap:18px}
.feature svg{flex:none}
.feature-text{color:var(--white);font-weight:800;font-style:italic;font-size:20px;letter-spacing:1.2px;line-height:24px}
.cta{
  position:absolute;left:754px;top:415px;width:406px;height:81px;border-radius:14px;
  background:var(--navy);color:var(--white);font-weight:900;font-size:27px;letter-spacing:1.4px;
  display:flex;align-items:center;justify-content:center;
}
.brand{position:absolute;left:870px;top:536px;width:176px;text-align:center;color:var(--white);font-weight:900;font-size:40px;letter-spacing:2px}
</style>
</head>
<body>

<h1 class="headline">ACCELERATE INCIDENT<br>INVESTIGATIONS &amp; LEARNINGS</h1>

<section class="app" aria-label="Investigation map workspace">
  <header class="app-bar">
    <span class="app-name">NORVEX</span>
    <span class="app-title">INVESTIGATION MAP</span>
    <span class="app-bar-right"><span class="mode-pill">FULL WRITE</span>Test Investigation<span class="app-gear"></span></span>
  </header>

  <div class="tool-btn" style="left:7px;top:27px"><svg width="9" height="9" viewBox="0 0 10 10"><circle cx="5" cy="5" r="5" fill="#111"/><path d="M6.5 5H3.5M5 3.5 3.5 5 5 6.5" stroke="#fff" stroke-width="1" fill="none"/></svg></div>
  <div class="tool-btn accent" style="left:7px;top:50px"><svg width="8" height="8" viewBox="0 0 10 10"><path d="M2 2l6 6M8 2 2 8" stroke="#fff" stroke-width="1.4"/></svg></div>
  <div class="tool-btn" style="left:491px;top:27px"><svg width="8" height="8" viewBox="0 0 10 10"><rect x="1" y="1" width="6" height="8" fill="none" stroke="#111"/><circle cx="7" cy="7" r="2" fill="none" stroke="#111"/></svg></div>
  <div class="tool-btn" style="left:514px;top:27px"><svg width="8" height="8" viewBox="0 0 10 10"><path d="M1 3V1h2M7 1h2v2M9 7v2H7M3 9H1V7" stroke="#111" fill="none"/><circle cx="5" cy="5" r="1.5" fill="#111"/></svg></div>
  <div class="tool-btn" style="left:537px;top:27px"><svg width="8" height="8" viewBox="0 0 10 10"><circle cx="4" cy="4" r="3" fill="none" stroke="#111" stroke-width="1.4"/><path d="M6 6l3 3" stroke="#111" stroke-width="1.6"/></svg></div>
  <div class="tool-btn" style="left:560px;top:27px"><svg width="8" height="8" viewBox="0 0 10 10"><rect x="2" y="1" width="6" height="3" fill="#111"/><rect x="0" y="4" width="10" height="4" rx="1" fill="#111"/><rect x="2" y="7" width="6" height="3" fill="#fff" stroke="#111"/></svg></div>
  <div class="tool-btn" style="left:583px;top:27px"><svg width="8" height="8" viewBox="0 0 10 10"><rect x="1" y="1" width="8" height="8" rx="2" fill="none" stroke="#111" stroke-width="1.2"/><path d="M5 3v4M3 5h4" stroke="#111" stroke-width="1.2"/></svg></div>

  <!-- sequence -->
  <div class="panel" style="left:50px;top:62px;width:352px;height:49px"><span class="panel-tag"></span>
    <div class="card footed" style="left:21px;top:10px;--c:#7fb8f0"></div>
    <div class="card footed" style="left:87px;top:10px;--c:#7fb8f0"></div>
    <div class="card footed" style="left:153px;top:10px;--c:#7fb8f0"></div>
    <div class="card footed" style="left:219px;top:10px;--c:#7fb8f0"></div>
    <div class="card footed" style="left:285px;top:10px;--c:#7fb8f0"></div>
  </div>
  <!-- people -->
  <div class="panel" style="left:50px;top:116px;width:105px;height:94px"><span class="panel-tag"></span>
    <div class="person" style="left:17px;top:11px"></div><div class="person" style="left:66px;top:11px"></div>
    <div class="person" style="left:17px;top:49px"></div><div class="person" style="left:66px;top:49px"></div>
  </div>
  <!-- task -->
  <div class="panel" style="left:165px;top:116px;width:60px;height:94px"><span class="panel-tag"></span>
    <div class="card chip" style="left:10px;top:11px;height:28px;--c:var(--orange)"></div>
    <div class="card chip" style="left:10px;top:54px;height:28px;--c:var(--orange)"></div>
  </div>
  <!-- factors -->
  <div class="panel" style="left:237px;top:116px;width:165px;height:94px"><span class="panel-tag"></span>
    <div class="card chip" style="left:10px;top:11px;height:32px;--c:var(--yellow)"></div>
    <div class="card chip" style="left:60px;top:11px;height:32px;--c:var(--yellow)"></div>
    <div class="card chip" style="left:110px;top:11px;height:32px;--c:var(--yellow)"></div>
    <div class="card chip" style="left:10px;top:51px;height:32px;--c:var(--purple)"></div>
    <div class="card chip" style="left:60px;top:51px;height:32px;--c:var(--purple)"></div>
    <div class="card chip" style="left:110px;top:51px;height:32px;--c:var(--purple)"></div>
  </div>
  <!-- controls -->
  <div class="panel" style="left:413px;top:62px;width:60px;height:148px"><span class="panel-tag"></span>
    <div class="card chip" style="left:10px;top:10px;height:30px;--c:var(--green)"></div>
    <div class="card chip" style="left:10px;top:58px;height:30px;--c:var(--green)"></div>
    <div class="card chip" style="left:10px;top:106px;height:30px;--c:var(--green)"></div>
  </div>
  <!-- evidence -->
  <div class="panel" style="left:484px;top:62px;width:60px;height:148px"><span class="panel-tag"></span>
    <div class="card" style="left:10px;top:10px;height:24px;--c:#bbb"></div>
    <div class="card" style="left:10px;top:58px;height:24px;--c:#bbb"></div>
    <div class="card" style="left:10px;top:106px;height:24px;--c:#bbb"></div>
  </div>
  <!-- bottom row -->
  <div class="panel" style="left:50px;top:221px;width:105px;height:49px"><span class="panel-tag"></span>
    <div class="card footed" style="left:55px;top:10px;--c:var(--red)"></div>
  </div>
  <div class="panel" style="left:165px;top:221px;width:159px;height:49px"><span class="panel-tag"></span>
    <div class="card" style="left:10px;top:10px;height:32px;border-top-width:8px;--c:var(--blue)"></div>
    <div class="card" style="left:60px;top:10px;height:32px;border-top-width:8px;--c:var(--blue)"></div>
    <div class="card" style="left:110px;top:10px;height:32px;border-top-width:8px;--c:var(--blue)"></div>
  </div>
  <div class="panel" style="left:336px;top:221px;width:290px;height:49px"><span class="panel-tag"></span>
    <div class="card" style="left:10px;top:10px;--c:var(--teal)"></div>
    <div class="card" style="left:86px;top:10px;--c:var(--teal)"></div>
    <div class="card" style="left:162px;top:10px;--c:var(--teal)"></div>
  </div>
</section>

<aside class="note note-collab">
  <span class="pin" style="left:50px;top:8px"></span>
  <h3>Collaboration</h3>
  <ul>
    <li>Assign control owners <span>&#9745;</span></li>
    <li>Make Recommendations <span>&#9745;</span></li>
    <li>Flexible brainstorming <span>&#9745;</span></li>
    <li>Keep investigation moving <span>&#9745;</span></li>
  </ul>
</aside>

<aside class="note note-map">
  <span class="pin" style="left:48px;top:6px"></span>
  <h3>Create Your Map</h3>
  <p>Capture evidence, sequence, factors and recommendations in <u>one</u> workflow</p>
</aside>

<div class="thumb thumb-home" aria-label="Website home screen">
  <p>Think through incidents,</p>
  <p class="muted">map the workflow, and</p>
  <p class="muted">act with clarity</p>
  <div class="btns"><i></i><i></i></div>
</div>
<div class="thumb thumb-style" aria-label="Card style editor">
  <div class="side"><div class="spectrum"></div></div>
  <div class="sheet">
    <div class="card" style="left:10px;top:14px;--c:var(--orange)"></div>
    <div class="card" style="left:10px;top:44px;--c:var(--purple)"></div>
    <div class="card" style="left:74px;top:14px;--c:var(--red)"></div>
    <div class="card" style="left:74px;top:44px;--c:var(--orange)"></div>
  </div>
</div>
<div class="thumb thumb-flow" aria-label="Connected investigation map">
  <svg width="118" height="78" viewBox="0 0 118 78">
    <rect x="14" y="16" width="90" height="2" fill="#111"/>
    <g fill="#f7821f"><rect x="14" y="28" width="10" height="4"/><rect x="30" y="28" width="10" height="4"/><rect x="14" y="44" width="10" height="4"/><rect x="30" y="44" width="10" height="4"/><rect x="14" y="58" width="10" height="4"/></g>
    <g fill="#7fb8f0"><rect x="46" y="24" width="10" height="4"/><rect x="46" y="38" width="10" height="4"/><rect x="46" y="52" width="10" height="4"/></g>
    <g fill="#e23b3b"><rect x="78" y="30" width="10" height="4"/><rect x="78" y="44" width="10" height="4"/></g>
    <g fill="#2fae5a"><rect x="94" y="24" width="10" height="4"/><rect x="94" y="36" width="10" height="4"/><rect x="94" y="48" width="10" height="4"/></g>
    <g stroke="#999" stroke-width=".5" fill="none"><path d="M56 26C68 26 68 32 78 32M56 40C68 40 68 46 78 46M88 32C92 32 92 26 94 26M88 46C92 46 92 38 94 38M88 46C92 46 92 50 94 50"/></g>
  </svg>
</div>

<div class="feature" style="top:192px">
  <svg width="44" height="36" viewBox="0 0 44 36" fill="#fff" stroke="#fff" stroke-width="2">
    <line x1="22" y1="18" x2="5" y2="6"/><line x1="22" y1="18" x2="36" y2="4"/><line x1="22" y1="18" x2="4" y2="26"/><line x1="22" y1="18" x2="40" y2="24"/><line x1="22" y1="18" x2="22" y2="33"/>
    <circle cx="22" cy="18" r="6"/><circle cx="5" cy="6" r="3"/><circle cx="36" cy="4" r="3"/><circle cx="4" cy="26" r="3"/><circle cx="40" cy="24" r="3"/><circle cx="22" cy="33" r="2.5"/>
  </svg>
  <span class="feature-text">Interactive investigation<br>maps</span>
</div>
<div class="feature" style="top:253px">
  <svg width="44" height="46" viewBox="0 0 44 46" fill="#fff">
    <rect x="10" y="6" width="24" height="38" fill="#fff" opacity=".8"/>
    <rect x="4" y="2" width="24" height="38"/>
    <g fill="#29dcfb"><rect x="8" y="9" width="12" height="2"/><rect x="8" y="15" width="16" height="2"/><rect x="8" y="21" width="16" height="2"/><rect x="8" y="27" width="12" height="2"/></g>
  </svg>
  <span class="feature-text">Generate reports instantly</span>
</div>
<div class="feature" style="top:314px">
  <svg width="44" height="40" viewBox="0 0 44 40" fill="#fff">
    <g stroke="#fff" stroke-width="2"><path d="M15 0v6M22 0v6M29 0v6M15 34v6M22 34v6M29 34v6M2 13h6M2 20h6M2 27h6M36 13h6M36 20h6M36 27h6"/></g>
    <rect x="8" y="6" width="28" height="28" rx="4"/>
    <text x="22" y="27" text-anchor="middle" font-family="Montserrat,sans-serif" font-weight="900" font-size="15" fill="#29dcfb">AI</text>
  </svg>
  <span class="feature-text">AI-assisted report building</span>
</div>

<div class="cta">GET FASTER INSIGHTS</div>

<div class="brand">NORVEX</div>

</body>
</html>
```